revised: 'eastgate joinwerks' logo -or- business card

we require a business card or a logo that can be used on a business card & other stationery

(i've just recently decided to open this contest up to logo designs as well - but if you have already been working on a card concept, please feel free to continue with it & submit!)

-

We design and build custom brackets and fixings for our customers and their castles, i.e. homes, offices, workshops, farms etc. Our products might be used to:
- brace or support structures, such as houses, decks, small bridges, etc.
- connect any building material to another
- or could simply be a unique piece that exists as a talking point

As part of our design process we would produce drawings/plans/blue prints/prototypes of the product. Our designs factor in multiple elements, from the materials being joined, the client's taste, and the overall durability demanded by the application - if necessary, the bracket may also be endorsed by a third party, such as a stuctural or mechanical engineer.

The build process takes part in our workshop and on the client's site - some elements may be manufactured off-site, depending on the design chosen and the materials used.

Our brackets are designed to our customers' tastes and could be made to be hidden within the structure or exposed to create interest. Our brackets can be large or small, or be neat with clean lines or take on more of an industrial look.
Updates

please note brief has been updated with a more specific description of our business activity

i have also added the final drawing that was used to water-jet the bracket shown in the photos

also, you will note i changed the title to 'logo + business card'

i don't expect a logo as a discrete artefact of the job, however, i expect that some or all elements on the face of the business card will lend themselves to the street sign (as stated in the original brief) as well as any future logo used on letter heads, invoices, etcetera

another update - changed the allowable entries to include logo's only, as well as business cards

Industry/Entity Type

Industrial

Requirements
Must have
• the face should have the name 'Eastgate Joinwerks' (or no/all-caps)

the number '75' in the logo, which will also be turned into a conservative (residential) street sign ('75' being a street number) - '75' should stand alone -OR- be readily identified by someone who has previously received a business card

i need to make this '75' and any associated 'framing', so it should be transferrable to cad/dxf for machining, laser/water-cutting, brazing/welding, etcet.

(on that note, the winning designer will be able to share their vision for this sign and we'll adhere to it ... within the realms of possibility! if you're happy with the result then you could include it in your portfolio)
Nice to have
• one side of the card needs a majority of space for quotes, hand-written information, etcet. so this side should be white or a light, complimentary colour suitable for black/blue pen

the following should appear somewhere on the card (there is no email or website) :
- name : First Last (Proprietor)
- mobile phone number : +61 (0) 498 761203
- abn: 58 907 614 230

any combination of the following (or equivalent) text:

* 'your castle' - this is slang for your house/place (i prefer this to 'home' as 1: it can apply to a place of business, and 2: for me at least, it conjurs images of wrought iron, brass, hardwood & stone)

* unique

* ...

```html
<!DOCTYPE html>
<html lang="en">
<head>
<meta charset="utf-8">
<title>Eastgate Joinwerks – business card concepts</title>
<link rel="stylesheet" href="https://fonts.googleapis.com/css2?family=Jost:wght@400;500;600;700&display=swap">
<style>
  :root {
    --sheet: #ebebeb;
    --card: #ffffff;
    --card-edge: #d6d6d6;
    --orange: #ee7f1b;
    --orange-deep: #e9641f;
    --ink: #1c1c1c;
    --slate: #5a5a5a;
    --rule: #bdbdbd;
    --label: #333333;
  }
  html, body {
    margin: 0;
    padding: 0;
    width: 1020px;
    height: 1200px;
    overflow: hidden;
    background: var(--sheet);
  }
  .sheet { display: block; width: 1020px; height: 1200px; }
  .sheet text { font-family: "Jost", "Futura", sans-serif; }
  .column-label { font-size: 19px; fill: var(--label); font-weight: 400; }
  .row-number { font-size: 20px; fill: var(--label); font-weight: 400; }
  .card-face { fill: var(--card); stroke: var(--card-edge); stroke-width: 1; }
  .band-orange { fill: var(--orange); }
  .band-deep { fill: var(--orange-deep); }
  .band-ink { fill: var(--ink); }
  .band-slate { fill: var(--slate); }
  .write-line { stroke: var(--rule); stroke-width: 1; }
  .company-name { font-weight: 700; font-size: 35px; fill: #ffffff; letter-spacing: 0.5px; }
  .company-name--tilted { font-size: 30px; }
  .company-name--dark { fill: var(--ink); font-size: 41px; }
  .person-name { font-weight: 600; font-size: 15.5px; fill: var(--ink); }
  .person-role { font-weight: 400; font-size: 11px; fill: var(--ink); letter-spacing: 0.3px; }
  .contact { font-weight: 400; font-size: 13.5px; fill: var(--ink); }
  .on-dark { fill: #ffffff; }
  .contact.on-dark { font-weight: 600; font-size: 12px; }
  .slogan { font-weight: 600; font-size: 15.5px; fill: #ffffff; letter-spacing: 0.3px; }
  .phone-icon { fill: none; stroke: var(--ink); stroke-width: 1; }
  .phone-icon.on-dark { stroke: #ffffff; fill: none; }
  .mark-spot { fill: var(--orange); }
  .mark-spot--deep { fill: var(--orange-deep); }
</style>
</head>
<body>
<svg class="sheet" viewBox="0 0 1000 1177" preserveAspectRatio="none" xmlns="http://www.w3.org/2000/svg">
  <defs>
    <clipPath id="clip-card3-front"><rect x="68" y="912" width="427" height="238" rx="24"/></clipPath>
    <clipPath id="clip-card3-back"><rect x="537" y="910" width="426" height="238" rx="24"/></clipPath>
    <symbol id="phone" viewBox="0 0 8 11"><rect x="0.5" y="0.5" width="7" height="10" rx="1"/><line x1="0.5" y1="8.5" x2="7.5" y2="8.5"/></symbol>
  </defs>

  <text class="column-label" x="252" y="46" text-anchor="middle">front</text>
  <text class="column-label" x="749" y="49" text-anchor="middle">back</text>

  <!-- Concept 1 -->
  <text class="row-number" x="36" y="76">1</text>
  <g class="card card--front">
    <rect class="card-face" x="61" y="58" width="425" height="238"/>
    <rect class="band-orange" x="61" y="58" width="425" height="60"/>
    <text class="company-name" x="273" y="101" text-anchor="middle">eastgate joinwerks</text>
    <circle class="mark-spot" cx="126" cy="188" r="38"/>
    <text class="person-name" x="207" y="150">YOUR NAME</text>
    <text class="person-role" x="207" y="166">PROPRIETOR</text>
    <use href="#phone" class="phone-icon" x="207" y="189" width="8" height="11"/>
    <text class="contact" x="220" y="200">+61 (0) 498 761203</text>
    <text class="contact" x="207" y="221">ABN: 58 907 614 230</text>
    <polygon class="band-orange" points="61,263 486,222 486,252 61,296"/>
    <polygon class="band-ink" points="61,296 486,252 486,296"/>
    <text class="slogan" x="305" y="263" text-anchor="middle" transform="rotate(-5.5 305 258)">YOUR SLOGAN HERE&#160;&#160;YOUR SLOGAN HERE</text>
  </g>
  <g class="card card--back">
    <rect class="card-face" x="529" y="61" width="426" height="237"/>
    <line class="write-line" x1="583" y1="112" x2="895" y2="112"/>
    <line class="write-line" x1="583" y1="142" x2="895" y2="142"/>
    <line class="write-line" x1="583" y1="172" x2="895" y2="172"/>
    <line class="write-line" x1="583" y1="202" x2="895" y2="202"/>
    <polygon class="band-orange" points="529,223 955,262 955,298 529,256"/>
    <polygon class="band-ink" points="529,256 955,298 529,298"/>
    <text class="slogan" x="734" y="263" text-anchor="middle" transform="rotate(5.3 734 258)">YOUR SLOGAN HERE&#160;&#160;YOUR SLOGAN HERE</text>
  </g>

  <!-- Concept 1a -->
  <text class="row-number" x="30" y="355">1a</text>
  <g class="card card--front">
    <rect class="card-face" x="62" y="331" width="426" height="244"/>
    <polygon class="band-orange" points="62,331 488,331 488,358 62,408"/>
    <text class="company-name company-name--tilted" x="260" y="366" text-anchor="middle" transform="rotate(-6.5 260 366)">eastgate joinwerks</text>
    <circle class="mark-spot" cx="128" cy="468" r="38"/>
    <g transform="rotate(-3 260 460)">
      <text class="person-name" x="208" y="428">YOUR NAME</text>
      <text class="person-role" x="208" y="444">PROPRIETOR</text>
      <use href="#phone" class="phone-icon" x="210" y="471" width="8" height="11"/>
      <text class="contact" x="223" y="482">+61 (0) 498 761203</text>
      <text class="contact" x="211" y="503">ABN: 58 907 614 230</text>
    </g>
    <polygon class="band-orange" points="62,552 488,500 488,530 62,575"/>
    <polygon class="band-ink" points="62,575 488,530 488,575"/>
    <text class="slogan" x="295" y="541" text-anchor="middle" transform="rotate(-5.5 295 536)">YOUR SLOGAN HERE&#160;&#160;YOUR SLOGAN HERE</text>
  </g>
  <g class="card card--back">
    <rect class="card-face" x="530" y="337" width="427" height="236"/>
    <line class="write-line" x1="584" y1="388" x2="897" y2="388"/>
    <line class="write-line" x1="584" y1="418" x2="897" y2="418"/>
    <line class="write-line" x1="584" y1="448" x2="897" y2="448"/>
    <line class="write-line" x1="584" y1="478" x2="897" y2="478"/>
    <polygon class="band-orange" points="530,500 957,540 957,573 530,533"/>
    <polygon class="band-ink" points="530,533 957,573 530,573"/>
    <text class="slogan" x="736" y="540" text-anchor="middle" transform="rotate(5.3 736 535)">YOUR SLOGAN HERE&#160;&#160;YOUR SLOGAN HERE</text>
  </g>

  <!-- Concept 2 -->
  <text class="row-number" x="38" y="652">2</text>
  <g class="card card--front">
    <rect class="card-face" x="67" y="633" width="425" height="237"/>
    <text class="company-name company-name--dark" x="100" y="680">eastgate</text>
    <text class="company-name company-name--dark" x="100" y="724">joinwerks</text>
    <rect class="band-orange" x="67" y="737" width="425" height="5"/>
    <rect class="band-ink" x="67" y="742" width="425" height="90"/>
    <circle class="mark-spot" cx="396" cy="737" r="56"/>
    <text class="person-name on-dark" x="133" y="767">YOUR NAME</text>
    <text class="person-role on-dark" x="133" y="782">PROPRIETOR</text>
    <use href="#phone" class="phone-icon on-dark" x="134" y="794" width="8" height="11"/>
    <text class="contact on-dark" x="146" y="803">+61 (0) 498 761203</text>
    <text class="contact on-dark" x="134" y="820">ABN: 58 907 614 230</text>
    <rect class="band-orange" x="67" y="832" width="425" height="38"/>
    <text class="slogan" x="271" y="857" text-anchor="middle">YOUR SLOGAN HERE</text>
  </g>
  <g class="card card--back">
    <rect class="card-face" x="537" y="634" width="426" height="237"/>
    <line class="write-line" x1="590" y1="686" x2="903" y2="686"/>
    <line class="write-line" x1="590" y1="716" x2="903" y2="716"/>
    <line class="write-line" x1="590" y1="746" x2="903" y2="746"/>
    <line class="write-line" x1="590" y1="776" x2="903" y2="776"/>
    <rect class="band-orange" x="537" y="833" width="426" height="38"/>
    <text class="slogan" x="737" y="859" text-anchor="middle">YOUR SLOGAN HERE</text>
  </g>

  <!-- Concept 3 -->
  <text class="row-number" x="38" y="934">3</text>
  <g class="card card--front">
    <rect class="card-face" x="68" y="912" width="427" height="238" rx="24"/>
    <g clip-path="url(#clip-card3-front)">
      <rect class="band-slate" x="68" y="912" width="427" height="62"/>
      <rect class="band-deep" x="68" y="1104" width="427" height="46"/>
    </g>
    <text class="company-name" x="282" y="957" text-anchor="middle">eastgate joinwerks</text>
    <circle class="mark-spot mark-spot--deep" cx="428" cy="1040" r="46"/>
    <text class="person-name" x="140" y="1006">YOUR NAME</text>
    <text class="person-role" x="140" y="1022">PROPRIETOR</text>
    <use href="#phone" class="phone-icon" x="140" y="1044" width="8" height="11"/>
    <text class="contact" x="153" y="1055">+61 (0) 498 761203</text>
    <text class="contact" x="140" y="1075">ABN: 58 907 614 230</text>
    <text class="slogan" x="270" y="1131" text-anchor="middle">YOUR SLOGAN HERE</text>
  </g>
  <g class="card card--back">
    <rect class="card-face" x="537" y="910" width="426" height="238" rx="24"/>
    <line class="write-line" x1="586" y1="962" x2="899" y2="962"/>
    <line class="write-line" x1="586" y1="992" x2="899" y2="992"/>
    <line class="write-line" x1="586" y1="1022" x2="899" y2="1022"/>
    <line class="write-line" x1="586" y1="1052" x2="899" y2="1052"/>
    <g clip-path="url(#clip-card3-back)">
      <rect class="band-deep" x="537" y="1102" width="426" height="46"/>
    </g>
    <text class="slogan" x="737" y="1129" text-anchor="middle">YOUR SLOGAN HERE</text>
  </g>
</svg>
</body>
</html>
```